TRENDY & MODERN BUSINESS CARD DESIGN for Media Company *

I need a minimalistic - clean - modern and professional business card layout and design for MEDIA & PHOTOGRAPHY STUDIO.

We do NOT have a logo, and not really looking for one - but rather excellent typography and design. We would consider the 3 as a focal point.

We do personal and commercial photography.

Target Market(s)

Personal and commercial photography clientele

Contact Information for Business Card

ZUB size - from zub.com / size guidelines are enclosed in the brief

Font styles to use
Sans Serif

Colors
f78f20
eda3c7
cee9f5
0555a3
e667a6
fbf289

Requirements
Must have
• Clean lines - Modern layout
Nice to have
• All blue background as an option - use color palette in brief please.
Should not have
• Old fashion fonts and regular fonts.

```html
<!DOCTYPE html>
<html lang="en">
<head>
<meta charset="utf-8">
<title>Lumen Harbor Studio – Business Card</title>
<link href="https://fonts.googleapis.com/css2?family=Lato:wght@400;700&display=swap" rel="stylesheet">
<style>
  :root {
    --page-bg: #ece8e2;
    --card-bg: #cde9f4;
    --ink: #1b6a93;
    --ink-soft: #2a7aa3;
    --shadow: rgba(40, 30, 20, 0.22);
  }
  * { margin: 0; padding: 0; box-sizing: border-box; }
  html, body {
    width: 1200px;
    height: 912px;
    overflow: hidden;
    background: var(--page-bg);
    font-family: "Lato", sans-serif;
    color: var(--ink);
  }
  .canvas {
    width: 1200px;
    height: 912px;
    display: flex;
    flex-direction: column;
    align-items: center;
    justify-content: center;
    gap: 48px;
  }
  .card {
    width: 700px;
    height: 400px;
    background: var(--card-bg);
    border-radius: 4px;
    box-shadow: 0 6px 18px var(--shadow);
    position: relative;
    padding: 44px 0 0 250px;
  }
  .brand-name {
    font-weight: 700;
    font-size: 28px;
    letter-spacing: -0.3px;
  }
  .brand-tagline {
    font-size: 20px;
    color: var(--ink-soft);
    margin-top: 4px;
  }
  .card-back .locations {
    margin-top: 64px;
    margin-left: -70px;
  }
  .locations-title {
    font-weight: 700;
    font-size: 26px;
    margin-left: 110px;
    letter-spacing: 0.3px;
  }
  .locations-row {
    display: flex;
    gap: 28px;
    font-size: 24px;
    margin-top: 14px;
  }
  .locations-row.second { margin-left: -58px; gap: 14px; }
  .city::before {
    content: "";
    display: inline-block;
    width: 15px;
    height: 15px;
    border-radius: 50%;
    background: var(--ink);
    margin-right: 8px;
    vertical-align: 2px;
  }
  .card-front { padding-left: 190px; }
  .card-front .brand { margin-left: 60px; }
  .person-name {
    font-weight: 700;
    font-size: 32px;
    margin-top: 22px;
  }
  .person-title {
    font-size: 20px;
    color: var(--ink-soft);
    margin-top: 2px;
  }
  .contact {
    font-size: 22px;
    color: var(--ink-soft);
    line-height: 1.35;
    margin-top: 22px;
  }
  .contact .address { margin-top: 22px; }
</style>
</head>
<body>
<main class="canvas">
  <section class="card card-back" aria-label="Card back">
    <div class="brand">
      <div class="brand-name">Lumen Harbor Studio</div>
      <div class="brand-tagline">Every Moment, Framed</div>
    </div>
    <div class="locations">
      <div class="locations-title">LOCATIONS</div>
      <div class="locations-row first">
        <span class="city">Denver</span>
        <span class="city">Boston</span>
      </div>
      <div class="locations-row second">
        <span class="city">Tulum</span>
        <span class="city">Austin</span>
        <span class="city">Lisboa</span>
      </div>
    </div>
  </section>

  <section class="card card-front" aria-label="Card front">
    <div class="brand">
      <div class="brand-name">Lumen Harbor Studio</div>
      <div class="brand-tagline">Every Moment, Framed</div>
    </div>
    <div class="person-name">Marisol Ortega</div>
    <div class="person-title">Founder &amp; Media Director</div>
    <div class="contact">
      <div class="phone">(813) 555-0142</div>
      <div class="email">mari@lumenharbor.com</div>
      <div class="address">480 Harbor Lane<br>7th Floor, Tampa, FL 33602</div>
    </div>
  </section>
</main>
</body>
</html>
```